Letterhead for TR Dealership
Harborline Vestra Orlan KTR
Project: Letterhead for TR Dealership
Letterhead for TR Dealership -
Creative Brief
Professional
Locations: Harborline Orlan KTR 4170 N. Tamsworth Avenue Carrowfield, OR 97511 Harborline Vestra KTR 1983 Pellway Hwy Denholm, OR 97534 Commercial & Fleet Department 4170 N. Tamsworth Avenue Carrowfield, OR 97511
(620) 555-0172 Carrowfield (620) 555-0148 Denholm
jmarvin@gohalvern.example
www.GoHalvern.example
Letterhead needs to reflect both locations and all brands. Vestra Orlan KTR check out our website: www.GoHalvern.example Red Fox is our company mascot. Can email logo design.

```html
<!DOCTYPE html>
<html lang="en">
<head>
<meta charset="utf-8">
<title>Harborline Vestra Orlan KTR – Stationery</title>
<link href="https://fonts.googleapis.com/css2?family=Roboto+Condensed:wght@400;700&family=Open+Sans:wght@400;600&display=swap" rel="stylesheet">
<style>
  :root{
    --backdrop:#e9e6e2;
    --paper:#ffffff;
    --ink:#1b1b1b;
    --muted:#555555;
    --brand-red:#9b1b2e;
    --band:#2a2626;
    --mascot:#c9c9c9;
  }
  *{box-sizing:border-box;margin:0;padding:0}
  html,body{width:1200px;height:926px;overflow:hidden}
  body{background:var(--backdrop);position:relative;font-family:"Open Sans",Arial,sans-serif;color:var(--ink)}
  .sheet{position:absolute;background:var(--paper);box-shadow:0 4px 14px rgba(0,0,0,.18);overflow:hidden}

  .brand{display:flex;align-items:center;gap:7px}
  .brand-square{background:var(--ink);flex:none}
  .brand-name{font-family:"Roboto Condensed",Arial,sans-serif;font-weight:700;color:var(--ink);letter-spacing:.5px;line-height:1}
  .brand-lines{font-family:"Roboto Condensed",Arial,sans-serif;color:var(--brand-red);letter-spacing:1px;line-height:1}
  .tagline{font-family:"Roboto Condensed",Arial,sans-serif;color:var(--muted);letter-spacing:.4px;white-space:nowrap}
  .tagline b{color:var(--brand-red)}
  .small{font-size:6.5px;line-height:1.45;color:var(--muted)}
  .label{color:var(--brand-red);font-weight:600}
  .rule{position:absolute;left:0;right:0;background:var(--brand-red)}
  .band{position:absolute;left:0;right:0;background:var(--band);color:#eee;font-family:"Roboto Condensed",Arial,sans-serif;letter-spacing:1.5px}

  /* Letterhead */
  .letterhead{left:68px;top:83px;width:484px;height:662px}
  .letterhead .brand{position:absolute;left:22px;top:18px}
  .letterhead .brand-square{width:34px;height:34px}
  .letterhead .brand-name{font-size:26px}
  .letterhead .brand-lines{font-size:8px;margin-top:3px}
  .letterhead .tagline{position:absolute;left:22px;top:58px;font-size:8px}
  .letterhead .contact{position:absolute;right:24px;top:20px;text-align:left}
  .mascot-mark{position:absolute;left:153px;top:218px;width:162px;height:200px;border-radius:8px;background:linear-gradient(180deg,#d3d3d3,var(--mascot))}
  .letterhead .addresses{position:absolute;left:22px;right:24px;top:598px;display:flex;justify-content:space-between}
  .letterhead .rule{top:644px;height:3px}
  .letterhead .band{top:647px;height:15px;font-size:8px;padding:3px 12px}

  /* Business card */
  .card{left:587px;top:83px;width:324px;height:226px;border-radius:8px}
  .card .brand{position:absolute;left:12px;top:12px}
  .card .brand-square{width:28px;height:28px}
  .card .brand-name{font-size:22px}
  .card .brand-lines{font-size:7px;margin-top:2px}
  .card .tagline{position:absolute;left:12px;top:46px;font-size:6.5px}
  .card .person{position:absolute;left:12px;top:92px}
  .card .person-name{font-family:"Roboto Condensed",Arial,sans-serif;font-weight:700;color:var(--brand-red);font-size:15px}
  .card .person-role{font-size:8px;font-weight:600}
  .card .person .small{margin-top:14px}
  .card .locations{position:absolute;left:196px;top:14px;width:120px;text-align:right}
  .card .rule{top:192px;height:3px}
  .card .band{top:195px;height:31px;font-size:9px;padding:10px 12px}

  /* Envelope */
  .envelope{left:587px;top:389px;width:578px;height:259px}
  .envelope .brand{position:absolute;left:16px;top:14px}
  .envelope .brand-square{width:32px;height:32px}
  .envelope .brand-name{font-size:26px}
  .envelope .brand-lines{font-size:8px;margin-top:3px}
  .envelope .tagline{position:absolute;left:16px;top:54px;font-size:9px}
  .envelope .locations{position:absolute;left:16px;top:84px}
  .envelope .rule{top:226px;height:4px}
  .envelope .band{top:230px;height:29px}
</style>
</head>
<body>

<section class="sheet letterhead">
  <div class="brand">
    <span class="brand-square"></span>
    <div>
      <div class="brand-name">HARBORLINE</div>
      <div class="brand-lines">VESTRA · ORLAN · KTR</div>
    </div>
  </div>
  <p class="tagline">YOUR HAULING PROS WHO ALWAYS <b>DELIVER!</b></p>
  <div class="contact small">
    P: (620) 555-0172 Carrowfield<br>
    (620) 555-0148 Denholm<br>
    E: jmarvin@gohalvern.example
  </div>
  <div class="mascot-mark" role="img" aria-label="Faint Red Fox mascot illustration"></div>
  <div class="addresses small">
    <p>Harborline Orlan KTR<br>4170 N. Tamsworth Avenue<br>Carrowfield, OR 97511</p>
    <p>Harborline Vestra KTR<br>1983 Pellway Hwy<br>Denholm, OR 97534</p>
    <p>Commercial &amp; Fleet Department<br>4170 N. Tamsworth Avenue<br>Carrowfield, OR 97511</p>
  </div>
  <div class="rule"></div>
  <div class="band">www.GoHalvern.example</div>
</section>

<section class="sheet card">
  <div class="brand">
    <span class="brand-square"></span>
    <div>
      <div class="brand-name">HARBORLINE</div>
      <div class="brand-lines">VESTRA · ORLAN · KTR</div>
    </div>
  </div>
  <p class="tagline">YOUR HAULING PROS WHO ALWAYS <b>DELIVER!</b></p>
  <div class="person">
    <div class="person-name">Name</div>
    <div class="person-role">Position</div>
    <p class="small">P: (620) 555-0172 Carrowfield<br>(620) 555-0148 Denholm<br>E: jmarvin@gohalvern.example</p>
  </div>
  <div class="locations small">
    <p class="label">Locations:</p><br>
    <p>Harborline Orlan KTR<br>4170 N. Tamsworth Avenue<br>Carrowfield, OR 97511</p><br>
    <p>Harborline Vestra KTR<br>1983 Pellway Hwy<br>Denholm, OR 97534</p><br>
    <p>Commercial &amp; Fleet Department<br>4170 N. Tamsworth Avenue<br>Carrowfield, OR 97511</p>
  </div>
  <div class="rule"></div>
  <div class="band">www.GoHalvern.example</div>
</section>

<section class="sheet envelope">
  <div class="brand">
    <span class="brand-square"></span>
    <div>
      <div class="brand-name">HARBORLINE</div>
      <div class="brand-lines">VESTRA · ORLAN · KTR</div>
    </div>
  </div>
  <p class="tagline">YOUR HAULING PROS WHO ALWAYS <b>DELIVER!</b></p>
  <div class="locations small">
    <p class="label">Locations:</p><br>
    <p>Harborline Orlan KTR<br>4170 N. Tamsworth Avenue<br>Carrowfield, OR 97511</p><br>
    <p>Harborline Vestra KTR<br>1983 Pellway Hwy<br>Denholm, OR 97534</p><br>
    <p>Commercial &amp; Fleet Department<br>4170 N. Tamsworth Avenue<br>Carrowfield, OR 97511</p>
  </div>
  <div class="rule"></div>
  <div class="band"></div>
</section>

</body>
</html>
```